Postcard Design

Commercial property agents in London.I have not used your company before but over the years have produced many postcards. simply a case of colour photos with small caption on the front with company logo with reverse just having B&W logo, half reserved for address and half empty for me to write personal message.

A5 is preferred size

Industry/Entity Type

It Company

Font styles to use
Sans Serif

```html
<!DOCTYPE html>
<html lang="en">
<head>
<meta charset="utf-8">
<title>Harwell Gate Postcard</title>
<link rel="stylesheet" href="https://fonts.googleapis.com/css2?family=PT+Sans:wght@400;700&family=Tenor+Sans&display=swap">
<style>
  :root {
    --green: #17662a;
    --white: #ffffff;
    --page: #ece8e2;
    --text: #555555;
    --text-dark: #333333;
    --panel: #f0f0f0;
    --rule: #d4d4d4;
  }
  * { margin: 0; padding: 0; box-sizing: border-box; }
  html, body { width: 955px; height: 1200px; overflow: hidden; }
  body { background: var(--page); position: relative; font-family: "PT Sans", sans-serif; }

  .card { position: absolute; background: var(--white); box-shadow: 3px 4px 8px rgba(0,0,0,0.25); }
  .card--front { left: 62px; top: 52px; width: 741px; height: 523px; }
  .card--back { left: 143px; top: 623px; width: 743px; height: 522px; }

  .photo { position: absolute; }
  .photo--corner-terrace { left: 0; top: 0; width: 350px; height: 326px; background: linear-gradient(180deg, #e4e6e9 0%, #f2f2f0 45%, #b9b6b0 80%, #6d6c6a 100%); }
  .photo--brick-house { left: 365px; top: 0; width: 181px; height: 158px; background: linear-gradient(180deg, #eef0f2 0%, #9a4b3b 35%, #7e4236 75%, #8d8a86 100%); }
  .photo--white-block { left: 560px; top: 0; width: 181px; height: 158px; background: linear-gradient(180deg, #e8ebe6 0%, #e9e5dc 50%, #5b6f5a 80%, #3a4a6a 100%); }
  .photo--glass-station { left: 365px; top: 170px; width: 181px; height: 156px; background: linear-gradient(180deg, #dfe4ea 0%, #9aa6b4 45%, #3c5a8a 70%, #77777a 100%); }
  .photo--stone-corner { left: 560px; top: 170px; width: 181px; height: 156px; background: linear-gradient(180deg, #e6ebef 0%, #b7a68c 40%, #a08c72 75%, #6e5a48 100%); }
  .photo--street-row { left: 0; top: 338px; width: 350px; height: 102px; background: linear-gradient(180deg, #c9c2b4 0%, #b5aa98 50%, #6e6a66 100%); }
  .photo--office-row { left: 365px; top: 338px; width: 376px; height: 102px; background: linear-gradient(180deg, #a9a9aa 0%, #8c8c8e 50%, #5f5f62 100%); }

  .band { position: absolute; background: var(--green); color: var(--white); }
  .band--front { left: 0; top: 452px; width: 741px; height: 71px; }

  .brand { position: absolute; display: flex; align-items: center; gap: 10px; color: var(--white); font-family: "PT Sans", sans-serif; font-weight: 400; line-height: 0.95; }
  .brand__mark { background: var(--white); flex: none; }
  .band--front .brand { left: 36px; top: 10px; font-size: 24px; }
  .band--front .brand__mark { width: 40px; height: 40px; }

  .front__headline { position: absolute; right: 17px; top: 8px; font-family: "Tenor Sans", sans-serif; font-size: 17.5px; }
  .front__call { position: absolute; right: 17px; top: 33px; display: flex; align-items: center; gap: 8px; font-size: 14px; }
  .front__phone { display: flex; align-items: center; gap: 6px; margin-left: 12px; font-weight: 700; font-size: 18px; }

  .back__header { left: 0; top: 0; width: 370px; height: 90px; }
  .back__header .brand { left: 40px; top: 22px; font-size: 30px; }
  .back__header .brand__mark { width: 52px; height: 52px; }

  .back__title { position: absolute; left: 21px; top: 100px; font-family: "Tenor Sans", sans-serif; font-size: 14.5px; color: var(--green); }
  .back__intro { position: absolute; left: 0; top: 122px; width: 372px; height: 102px; background: var(--panel); padding: 10px 0 0 23px; font-size: 9.6px; line-height: 12.4px; color: var(--text); }
  .back__intro p + p { margin-top: 4px; }

  .contact { position: absolute; left: 378px; top: 18px; font-size: 9.8px; line-height: 13.4px; color: var(--text); }
  .contact__label { margin-bottom: 7px; }
  .contact__name { font-weight: 700; }

  .stamp { position: absolute; left: 614px; top: 19px; width: 103px; height: 80px; border: 1px solid var(--rule); }
  .address-line { position: absolute; left: 502px; width: 215px; border-top: 1px solid var(--rule); }

  .band--back-footer { left: 0; top: 484px; width: 743px; height: 38px; font-size: 14.5px; }
  .footer__item { position: absolute; top: 9px; display: flex; align-items: center; gap: 6px; }
  .footer__item svg { fill: var(--white); }
</style>
</head>
<body>

<section class="card card--front">
  <div class="photo photo--corner-terrace" role="img" aria-label="Photo of a white stucco corner terrace on a London street"></div>
  <div class="photo photo--brick-house" role="img" aria-label="Photo of a red brick townhouse office"></div>
  <div class="photo photo--white-block" role="img" aria-label="Photo of a white office block above a cafe terrace"></div>
  <div class="photo photo--glass-station" role="img" aria-label="Photo of a glass office building over a station entrance"></div>
  <div class="photo photo--stone-corner" role="img" aria-label="Photo of a stone corner office building"></div>
  <div class="photo photo--street-row" role="img" aria-label="Photo of a row of shops under a period stone facade"></div>
  <div class="photo photo--office-row" role="img" aria-label="Photo of a street of modern office frontages"></div>

  <div class="band band--front">
    <div class="brand"><span class="brand__mark"></span><span>Harwell<br>Gate</span></div>
    <div class="front__headline">Commercial Property Agents in West End of London</div>
    <div class="front__call">
      <span>Call today for your FREE estimate!</span>
      <span class="front__phone">
        <svg width="16" height="16" viewBox="0 0 16 16"><circle cx="8" cy="8" r="7" fill="none" stroke="#fff" stroke-width="1.4"/><path d="M5.5 4.5 L7 6 L6.3 7 Q7.3 8.9 9 9.7 L10 9 L11.5 10.5 L10.5 11.5 Q6.5 11 4.5 5.5 Z" fill="#fff"/></svg>
        020 7946 0321
      </span>
    </div>
  </div>
</section>

<section class="card card--back">
  <div class="band back__header">
    <div class="brand"><span class="brand__mark"></span><span>Harwell<br>Gate</span></div>
  </div>
  <h2 class="back__title">Commercial Property Agents in West End of London</h2>
  <div class="back__intro">
    <p>Harwell Gate are specialist commercial property agents in business property<br>for rent and office space leasing in London, with many letting opportunities in<br>the West End, Mayfair and Victoria.</p>
    <p>Our expertise as commercial property agents covers Office Leasing and Sales,<br>Office Search and Acquisition, Rent Reviews, Lease Renewals and Serviced Offices<br>in London.</p>
  </div>

  <address class="contact" style="font-style:normal">
    <div class="contact__label">Contact Us</div>
    <div class="contact__name">Daniel Harwell MRICS</div>
    <div>Harwell Gate</div>
    <div>14 Linden Mews</div>
    <div>London W1X 7QT</div>
  </address>

  <div class="stamp"></div>
  <div class="address-line" style="top:173px"></div>
  <div class="address-line" style="top:211px"></div>
  <div class="address-line" style="top:248px"></div>
  <div class="address-line" style="top:285px"></div>
  <div class="address-line" style="top:323px"></div>

  <div class="band band--back-footer">
    <div class="footer__item" style="left:29px">
      <svg width="14" height="14" viewBox="0 0 14 14"><circle cx="7" cy="7" r="6" fill="none" stroke="#fff" stroke-width="1.4"/><path d="M1 7 H13 M7 1 Q3.5 7 7 13 M7 1 Q10.5 7 7 13" fill="none" stroke="#fff" stroke-width="1"/></svg>
      www.harwellgate.com
    </div>
    <div class="footer__item" style="left:315px">
      <svg width="12" height="12" viewBox="0 0 12 12"><path d="M2 1 L4.5 3.5 L3.4 5 Q4.8 7.4 7 8.6 L8.5 7.5 L11 10 L9.5 11.5 Q3 11 0.5 2.5 Z"/></svg>
      020 7946 0321
    </div>
    <div class="footer__item" style="left:548px">
      <svg width="14" height="12" viewBox="0 0 14 12"><path d="M1 5 L7 1 L13 5 V11 H1 Z M2.5 6 L7 9 L11.5 6" fill="#fff" stroke="#17662a" stroke-width="1"/></svg>
      dh@harwellgate.com
    </div>
  </div>
</section>

</body>
</html>
```